Medical Device Packaging Project 3 of 5

We are a medical device startup company needing packaging for a total of 5 device brands. This is posting 3 of 5 and the device name is "Vosmi"

Vosmi is an intraocular lens for use in cataract surgery. The target market is Chinese ophthalmologists. The box should be sophisticated and upmarket.

The company name is Kemberly Optics, I have included the logo in the uploaded files section. You should include the logo on the box.

I have uploaded a sample lens boxes from other companies that demonstrate the information needed to be contained on the box in terms of address, warnings, symbols, etc.

I have also uploaded the blank dieline of the boxes

You are welcome and encouraged to also submit to projects 1, 2, 4, and 5 as well. The same rules and expectations apply.

Requirements
Should not have
• Should not have any images of an eye or any bionic/futuristic feel to the design
• Note that the tavilens box is for text reference only. You may use the lens image but the futuristic/bionic look is NOT what we are going for with this brand. It should be traditional upmarket medical device artwork.

```html
<!DOCTYPE html>
<html lang="en">
<head>
<meta charset="utf-8">
<title>Vosmi – Kemberly Optics packaging</title>
<link rel="stylesheet" href="https://fonts.googleapis.com/css2?family=Montserrat:wght@400;500;700&family=Open+Sans:wght@400;700&display=swap">
<style>
  :root {
    --page: #ffffff;
    --band: #434447;
    --side: #3b3c3f;
    --band-edge: #36373a;
    --mist-light: #c9d5dc;
    --mist-mid: #93a7b3;
    --mist-dark: #6e8592;
    --lens-light: #e6eef3;
    --lens-mid: #b9cbd6;
    --text-light: #f2f4f5;
    --text-soft: #d9dde0;
    --icon: #b9bdc1;
    --rule: #c8ccd0;
  }
  * { box-sizing: border-box; margin: 0; padding: 0; }
  html, body {
    width: 1200px;
    height: 914px;
    overflow: hidden;
    background: var(--page);
  }
  .canvas {
    position: relative;
    width: 1200px;
    height: 914px;
  }
  .box-flat {
    position: absolute;
    left: 125px;
    top: 165px;
    height: 584px;
    display: flex;
    box-shadow: 0 18px 40px rgba(0, 0, 0, 0.12);
  }
  .box-front {
    width: 820px;
    height: 100%;
    display: flex;
  }
  .mist-panel { height: 100%; }
  .mist-panel--left {
    width: 161px;
    background:
      radial-gradient(circle at 40% 30%, rgba(255,255,255,0.45) 0, rgba(255,255,255,0) 28%),
      radial-gradient(circle at 70% 65%, rgba(255,255,255,0.3) 0, rgba(255,255,255,0) 30%),
      linear-gradient(160deg, var(--mist-mid), var(--mist-dark) 55%, var(--mist-mid));
  }
  .mist-panel--right {
    width: 308px;
    background:
      radial-gradient(circle at 55% 35%, rgba(255,255,255,0.55) 0, rgba(255,255,255,0) 35%),
      radial-gradient(circle at 30% 75%, rgba(255,255,255,0.35) 0, rgba(255,255,255,0) 30%),
      linear-gradient(165deg, var(--mist-light), var(--mist-mid) 50%, var(--mist-dark));
  }
  .brand-band {
    position: relative;
    width: 351px;
    height: 100%;
    background: var(--band);
    border-left: 1px solid var(--band-edge);
    border-right: 1px solid var(--band-edge);
  }
  .company-name {
    position: absolute;
    top: 108px;
    left: 0;
    width: 100%;
    display: flex;
    align-items: center;
    justify-content: center;
    gap: 10px;
    font-family: "Montserrat", sans-serif;
    font-weight: 500;
    font-size: 28px;
    letter-spacing: 1.5px;
    color: var(--text-light);
  }
  .company-mark {
    width: 12px;
    height: 12px;
    border-radius: 50%;
    background: var(--text-light);
  }
  .lens-figure {
    position: absolute;
    left: 20px;
    top: 195px;
    width: 270px;
    height: 290px;
  }
  .product-name {
    position: absolute;
    left: 50px;
    top: 455px;
    font-family: "Montserrat", sans-serif;
    font-weight: 700;
    font-size: 46px;
    letter-spacing: 5px;
    line-height: 1;
    color: var(--text-light);
  }
  .product-desc {
    position: absolute;
    left: 48px;
    top: 515px;
    width: 190px;
    padding: 7px 0 9px;
    border-top: 1px solid var(--rule);
    border-bottom: 1px solid var(--rule);
    font-family: "Open Sans", sans-serif;
    font-size: 14px;
    line-height: 1.25;
    color: var(--text-soft);
    text-align: center;
  }
  .product-desc strong {
    font-weight: 700;
    color: var(--text-light);
  }
  .box-side {
    position: relative;
    width: 130px;
    height: 100%;
    background: var(--side);
    border-left: 1px solid var(--band-edge);
  }
  .symbol-column {
    position: absolute;
    top: 40px;
    right: 28px;
    display: flex;
    flex-direction: column;
    align-items: center;
    gap: 26px;
  }
  .symbol {
    width: 14px;
    height: 14px;
    border: 1.5px solid var(--icon);
    border-radius: 50%;
  }
  .symbol--triangle {
    border: none;
    border-radius: 0;
    width: 0;
    height: 0;
    border-left: 7px solid transparent;
    border-right: 7px solid transparent;
    border-bottom: 13px solid var(--icon);
  }
  .sterile-tag {
    position: absolute;
    top: 250px;
    right: 22px;
    width: 22px;
    height: 64px;
    border: 1px solid var(--icon);
    display: flex;
    align-items: center;
    justify-content: center;
  }
  .sterile-tag span {
    transform: rotate(-90deg);
    white-space: nowrap;
    font-family: "Open Sans", sans-serif;
    font-size: 8px;
    letter-spacing: 1px;
    color: var(--icon);
  }
  .side-name {
    position: absolute;
    left: 50%;
    bottom: 170px;
    transform: translateX(-50%) rotate(90deg);
    white-space: nowrap;
    display: flex;
    align-items: center;
    gap: 8px;
    font-family: "Montserrat", sans-serif;
    font-weight: 500;
    font-size: 24px;
    letter-spacing: 1.5px;
    color: var(--text-light);
  }
</style>
</head>
<body>
  <main class="canvas">
    <div class="box-flat">
      <section class="box-front">
        <div class="mist-panel mist-panel--left" role="img" aria-label="Soft blue-grey bokeh light backdrop"></div>

        <div class="brand-band">
          <div class="company-name"><span class="company-mark"></span>Kemberly Optics</div>

          <svg class="lens-figure" viewBox="0 0 270 290" role="img" aria-label="Illustration of the intraocular lens with its two curved haptics">
            <defs>
              <radialGradient id="lens-fill" cx="45%" cy="40%" r="65%">
                <stop offset="0" stop-color="#e6eef3"/>
                <stop offset="1" stop-color="#b9cbd6"/>
              </radialGradient>
            </defs>
            <ellipse cx="145" cy="140" rx="92" ry="88" fill="url(#lens-fill)"/>
          </svg>

          <h1 class="product-name">VOSMI</h1>
          <p class="product-desc"><strong>Intraocular lens</strong> for use<br>in cataract surgery</p>
        </div>

        <div class="mist-panel mist-panel--right" role="img" aria-label="Soft blue-grey bokeh light backdrop"></div>
      </section>

      <aside class="box-side">
        <div class="symbol-column">
          <span class="symbol"></span>
          <span class="symbol"></span>
          <span class="symbol"></span>
          <span class="symbol symbol--triangle"></span>
        </div>
        <div class="sterile-tag"><span>STERILE EO</span></div>
        <div class="side-name"><span class="company-mark"></span>Kemberly Optics</div>
      </aside>
    </div>
  </main>
</body>
</html>
```